New Advertising Company Business Card

A two sided business card. One side with logo only and the other side with my information and maybe my logo again. Looking for something unique and creative, but not too busy. Info would include my name(Marcus Fenley), President, phone number, address, email address, and website. LOGO IS THE BLUE AND WHITE ONE.

Target Market(s)

CEO/VP Level Audience

Industry/Entity Type

Business

Contact Information for Business Card

In Description.

```html
<!DOCTYPE html>
<html lang="en">
<head>
<meta charset="UTF-8">
<title>Crestway Advertising — Business Card</title>
<link href="https://fonts.googleapis.com/css2?family=Montserrat:wght@400;500;600;700&display=swap" rel="stylesheet">
<style>
  :root {
    --brand-blue: #2a7dc4;
    --brand-blue-dark: #1f6db2;
    --ink: #3a3a3c;
    --paper: #ffffff;
    --backdrop: #2b2b2d;
  }
  * { box-sizing: border-box; margin: 0; padding: 0; }
  html, body { width: 1200px; height: 930px; overflow: hidden; }
  body {
    background: var(--backdrop);
    font-family: "Montserrat", sans-serif;
    position: relative;
  }
  .card {
    position: absolute;
    width: 560px;
    height: 320px;
    box-shadow: 0 14px 30px rgba(0,0,0,.45);
    overflow: hidden;
  }

  /* Front side */
  .card--front {
    left: 110px; top: 90px;
    background: var(--brand-blue);
  }
  .front-frame {
    position: absolute;
    inset: 16px;
    border: 1.5px solid rgba(255,255,255,.9);
  }
  .front-wordmark {
    position: absolute;
    left: 0; right: 0; top: 108px;
    text-align: center;
    color: var(--paper);
    font-weight: 600;
    line-height: 1;
  }
  .front-wordmark .name-main { display: block; font-size: 46px; letter-spacing: 4px; }
  .front-wordmark .name-sub  { display: block; font-size: 15px; letter-spacing: 9px; margin-top: 10px; padding-left: 9px; }
  .front-url {
    position: absolute;
    left: 50%; bottom: 8px;
    transform: translateX(-50%);
    background: var(--brand-blue);
    color: var(--paper);
    font-size: 13px;
    font-weight: 500;
    padding: 0 8px;
    letter-spacing: .5px;
  }

  /* Back side */
  .card--back {
    left: 530px; top: 500px;
    background: var(--paper);
  }
  .back-wordmark {
    position: absolute;
    left: 40px; top: 112px;
    width: 230px;
    text-align: center;
    color: var(--brand-blue);
    font-weight: 600;
    line-height: 1;
  }
  .back-wordmark .name-main { display: block; font-size: 34px; letter-spacing: 3px; }
  .back-wordmark .name-sub  { display: block; font-size: 11.5px; letter-spacing: 6.5px; margin-top: 9px; padding-left: 6px; }
  .divider {
    position: absolute;
    left: 292px; top: 62px;
    width: 1.5px; height: 150px;
    background: var(--brand-blue);
  }
  .contact {
    position: absolute;
    left: 318px; top: 66px;
  }
  .contact__name {
    color: var(--brand-blue);
    font-size: 22px;
    font-weight: 600;
    letter-spacing: -.3px;
    text-transform: uppercase;
  }
  .contact__title {
    color: var(--ink);
    font-size: 12.5px;
    font-weight: 500;
    letter-spacing: .5px;
    margin-top: 3px;
  }
  .contact__dash {
    width: 22px; height: 3px;
    background: var(--brand-blue);
    margin: 14px 0 16px;
  }
  .contact__list { list-style: none; }
  .contact__list li {
    display: flex; align-items: center; gap: 9px;
    color: var(--ink);
    font-size: 12.5px;
    line-height: 18px;
  }
  .contact__list svg { width: 10px; height: 10px; flex: none; }
  .address-band {
    position: absolute;
    left: 0; right: 0; bottom: 0;
    height: 34px;
    background: var(--brand-blue-dark);
    color: var(--paper);
    font-size: 12px;
    letter-spacing: .3px;
    display: flex; align-items: center; justify-content: flex-end;
    padding-right: 50px;
  }
</style>
</head>
<body>

  <section class="card card--front" aria-label="Card front">
    <div class="front-frame"></div>
    <div class="front-wordmark">
      <span class="name-main">CRESTWAY</span>
      <span class="name-sub">ADVERTISING</span>
    </div>
    <span class="front-url">www.crestway.com</span>
  </section>

  <section class="card card--back" aria-label="Card back">
    <div class="back-wordmark">
      <span class="name-main">CRESTWAY</span>
      <span class="name-sub">ADVERTISING</span>
    </div>
    <div class="divider"></div>
    <div class="contact">
      <h1 class="contact__name">Marcus Fenley</h1>
      <p class="contact__title">PRESIDENT</p>
      <div class="contact__dash"></div>
      <ul class="contact__list">
        <li>
          <svg viewBox="0 0 10 10" aria-hidden="true"><rect x="2.5" y="0.8" width="5" height="8.4" rx="1" fill="none" stroke="#3a3a3c" stroke-width="1"/><circle cx="5" cy="7.6" r=".6" fill="#3a3a3c"/></svg>
          +63 917 555 0142
        </li>
        <li>
          <svg viewBox="0 0 10 10" aria-hidden="true"><rect x="0.8" y="2" width="8.4" height="6" fill="none" stroke="#3a3a3c" stroke-width="1"/><path d="M0.8 2 L5 5.5 L9.2 2" fill="none" stroke="#3a3a3c" stroke-width="1"/></svg>
          info@crestway.com
        </li>
        <li>
          <svg viewBox="0 0 10 10" aria-hidden="true"><circle cx="5" cy="5" r="4.2" fill="none" stroke="#3a3a3c" stroke-width="1"/><ellipse cx="5" cy="5" rx="1.8" ry="4.2" fill="none" stroke="#3a3a3c" stroke-width=".8"/><path d="M0.8 5 H9.2" stroke="#3a3a3c" stroke-width=".8"/></svg>
          www.crestway.com
        </li>
      </ul>
    </div>
    <div class="address-band">Unit 8, The Harwell Centre, Ashby Lane, Milford, Herts AL9 4QR</div>
  </section>

</body>
</html>
```